Slide-Banner für Webseite
Zielgruppe
Lettershop Mailings, kuvertierte Mailings, Selfmailer, Postkarten, Adressierung. Druckerei mit Versand
Aufgabenstellung
Auf der Startseite im oben ein Kind ein Banner mit einem Kind zu sehen.
Hierfür hätte ich gerne drei neue Banner:
1. April Angebot: 100 Euro Gutschein (ab 500 Euro bestellwert)
2. Persönlicher Ansprechpartner - Von der Bestellung bis zur Postauflieferung
3. Lettershop - Mailing - Print - Mailings online kalkulieren und direkt bestellen (das Kind muss weg)
http://kurzlnk.de/Xq7TzR

```html
<!DOCTYPE html>
<html lang="de">
<head>
<meta charset="utf-8">
<title>Lettershop – Mailing – Print</title>
<link href="https://fonts.googleapis.com/css2?family=PT+Serif&family=Nunito:wght@800&display=swap" rel="stylesheet">
<style>
  :root {
    --lawn-dark: #4f6a36;
    --lawn-light: #8aa264;
    --path-grey: #b9b3a8;
    --path-light: #d2cdc4;
    --panel-bg: rgba(22, 20, 18, 0.78);
    --accent-green: #1f9a2b;
    --text-white: #ffffff;
  }
  html, body {
    margin: 0;
    padding: 0;
    overflow: hidden;
  }
  .banner {
    position: relative;
    width: 1200px;
    height: 211px;
    overflow: hidden;
  }
  .banner__scene {
    position: absolute;
    inset: 0;
    background:
      linear-gradient(90deg, rgba(40, 50, 30, 0.35) 0%, rgba(255, 255, 255, 0) 40%, rgba(230, 230, 225, 0.25) 100%),
      linear-gradient(180deg, var(--lawn-dark) 0%, var(--lawn-light) 48%, var(--path-grey) 72%, var(--path-light) 100%);
  }
  .banner__panel {
    position: absolute;
    left: 469px;
    top: 40px;
    width: 691px;
    height: 120px;
    background: var(--panel-bg);
  }
  .banner__services {
    position: absolute;
    left: 24px;
    top: 10px;
    margin: 0;
    display: flex;
    align-items: center;
    font-family: "PT Serif", serif;
    font-weight: 400;
    font-size: 27px;
    letter-spacing: 3px;
    color: var(--text-white);
    white-space: nowrap;
  }
  .banner__marker {
    display: inline-block;
    width: 17px;
    height: 17px;
    background: var(--accent-green);
    margin-right: 16px;
  }
  .banner__service + .banner__marker {
    margin-left: 14px;
  }
  .banner__claim {
    position: absolute;
    left: 0;
    right: 0;
    top: 60px;
    margin: 0;
    text-align: center;
    font-family: "Nunito", sans-serif;
    font-weight: 800;
    font-size: 18px;
    line-height: 23px;
    letter-spacing: 1.6px;
    color: var(--text-white);
  }
</style>
</head>
<body>
  <div class="banner">
    <div class="banner__scene" role="img" aria-label="Foto: Briefkasten am Holzpfosten vor Rasen, Gartenweg und weißem Haus"></div>
    <div class="banner__panel">
      <h1 class="banner__services">
        <span class="banner__marker"></span><span class="banner__service">LETTERSHOP</span>
        <span class="banner__marker"></span><span class="banner__service">MAILING</span>
        <span class="banner__marker"></span><span class="banner__service">PRINT</span>
      </h1>
      <p class="banner__claim">Mailings online kalkulieren<br>und direkt bestellen</p>
    </div>
  </div>
</body>
</html>
```